Web Design for Independent Pet Supply shop.

Larkfield Critter Depot is a locally owned and operated premium natural pet food store and supply company with 2 thriving retail stores in Bend, Oregon, and a home delivery service. The pet food offered is the best on the market and may be described as “holistic”. Also on offer is a vast selection of toys, training tools, treats, and other supplies, as well as dog washing services that range from "do-it yourself" to "spa." Current site: LarkfieldCritterDepot.com. They need a new, updated and responsive site.
Likes:
Tovmira.com: Natural colors, not loud, pages in motion, simple & clean but very informative.
Dunmoregale.com: Everything in simple big colorful blocks. The specials run across the top and in motion. This site looks very professional but simple. The information is available several different places.
Quillbarrow.com: Again big blocks through out. Very Fun and inviting. Tons of information with videos and recipes and testimonials. Pleasant feel and colors as well.
Dislikes:
Zinvor.com: Looks cheap, hate the colors, very busy and over whelming. Hate the old style header bar going across with options. Too many printed words instead of fun images.
Colors should be "natural" tones, warm and soothing. Deep dark blue and greys with earthy wood color.
Do Not Use: Blue violet, violet, red violet

```html
<!DOCTYPE html>
<html lang="en">
<head>
<meta charset="utf-8">
<title>Larkfield Critter Depot</title>
<link href="https://fonts.googleapis.com/css2?family=Open+Sans:ital,wght@0,400;0,600;0,700;1,400&family=Roboto+Condensed:wght@400;700&family=Oswald:wght@500;600&family=Montserrat:wght@800&display=swap" rel="stylesheet">
<style>
:root{
  --wood:#b98a4a;
  --wood-light:#d2b883;
  --wood-text:#b5803f;
  --ink:#2b2b2b;
  --body:#3a3a3a;
  --paper:#f6f6f6;
  --feature-bg:#f3f3f3;
  --photos-bg:#e6e6e6;
  --news-bg:#262626;
  --footer-bg:#e9e9e9;
  --bar-bg:#2b2b2b;
  --white:#ffffff;
}
*{margin:0;padding:0;box-sizing:border-box}
html,body{width:1200px;height:2171px;overflow:hidden}
body{position:relative;background:var(--paper);font-family:"Open Sans",Arial,sans-serif;color:var(--body)}
.abs{position:absolute}

/* header */
.site-header{left:0;top:0;width:1200px;height:120px;background:var(--paper)}
.brand{display:flex;align-items:center;gap:10px;font-family:"Oswald",sans-serif;font-weight:600;color:var(--wood-text);text-transform:uppercase;white-space:nowrap}
.brand-dot{width:18px;height:18px;border-radius:50%;background:var(--wood-text);flex:none}
.brand--head{left:232px;top:40px;font-size:26px}
.tagline{left:593px;top:52px;font-size:10.5px;font-style:italic;color:#444;text-decoration:underline}
.phone-icon{left:812px;top:42px;width:38px;height:38px;border-radius:50%;background:var(--wood);display:flex;align-items:center;justify-content:center}
.phone-number{left:861px;top:51px;font-size:14px;font-weight:600;color:#333}

/* nav */
.main-nav{left:0;top:120px;width:1200px;height:49px;background:var(--wood)}
.nav-home{left:229px;top:120px;width:85px;height:49px;background:var(--wood-light)}
.nav-item{top:120px;height:49px;line-height:49px;font-size:14px;color:var(--white);transform:translateX(-50%);white-space:nowrap}
.nav-item--active{color:#333}
.nav-item--big{font-size:16px}

/* hero */
.hero{left:0;top:169px;width:1200px;height:442px;
  background:
    radial-gradient(circle at 430px 78px,rgba(255,252,220,0.95) 0 30px,rgba(255,240,190,0.35) 40px,rgba(255,240,190,0) 60px),
    radial-gradient(circle at 567px 78px,rgba(255,252,220,0.95) 0 30px,rgba(255,240,190,0.35) 40px,rgba(255,240,190,0) 60px),
    radial-gradient(circle at 745px 60px,rgba(255,240,200,0.75) 0 28px,rgba(255,240,200,0) 52px),
    radial-gradient(circle at 188px 48px,rgba(200,30,30,0.75) 0 26px,rgba(200,30,30,0) 44px),
    radial-gradient(circle at 378px 42px,rgba(190,30,30,0.55) 0 28px,rgba(190,30,30,0) 48px),
    radial-gradient(circle at 1140px 100px,rgba(230,20,20,0.85) 0 22px,rgba(230,20,20,0) 38px),
    radial-gradient(circle at 1190px 60px,rgba(230,20,20,0.7) 0 22px,rgba(230,20,20,0) 36px),
    radial-gradient(circle at 60px 90px,rgba(200,140,60,0.35) 0 20px,rgba(200,140,60,0) 50px),
    radial-gradient(ellipse 520px 140px at 640px 150px,rgba(60,170,230,0.85),rgba(40,120,180,0.35) 60%,rgba(40,120,180,0) 100%),
    linear-gradient(180deg,#141b24 0%,#1e3346 34%,#2a2520 46%,#5e4735 58%,#3a2c22 74%,#1c1612 100%);}
.hero-dog{left:630px;top:188px;width:430px;height:442px;
  background:
    radial-gradient(ellipse 120px 150px at 170px 150px,rgba(250,246,240,0.95),rgba(250,246,240,0) 100%),
    radial-gradient(ellipse 240px 260px at 180px 210px,#b8652b 0%,#a45a28 50%,rgba(164,90,40,0) 100%),
    radial-gradient(ellipse 220px 70px at 260px 400px,rgba(245,240,235,0.9),rgba(245,240,235,0) 100%);}
.hero-arrow{top:352px;width:80px;height:75px;display:flex;align-items:center;justify-content:center}
.hero-arrow--left{left:0;background:rgba(0,0,0,0.35)}
.hero-arrow--right{left:1120px}
.hero-title{left:242px;top:322px;font-family:"Montserrat",sans-serif;font-weight:800;font-size:25px;color:var(--white);text-transform:uppercase;white-space:nowrap}
.hero-title span{color:var(--wood)}
.hero-text{left:246px;top:374px;width:500px;font-size:10.4px;line-height:14px;color:var(--white)}
.btn-hero{left:243px;top:449px;width:123px;height:39px;background:var(--wood);color:var(--white);font-size:13px;display:flex;align-items:center;justify-content:center;text-transform:uppercase}
.hero-dot{top:566px;width:13px;height:13px;border-radius:50%;background:#4c4c4c}
.hero-dot--on{background:#2f7fb6}

/* features */
.features{left:0;top:611px;width:1200px;height:294px;background:var(--feature-bg);border-bottom:1px solid #d6d6d6}
.feature{top:669px;width:211px}
.feature-icon{width:58px;height:58px;border-radius:50%;background:var(--wood-light);display:flex;align-items:center;justify-content:center;position:absolute;left:0;top:0}
.feature-title{position:absolute;left:71px;top:17px;font-family:"Roboto Condensed",sans-serif;font-weight:700;font-size:19px;color:#2a2a2a;white-space:nowrap}
.feature-text{position:absolute;left:2px;top:70px;width:211px;font-size:10.1px;line-height:13.8px;letter-spacing:-0.1px;text-align:justify;color:#333}
.feature-more{position:absolute;left:0;top:160px;width:211px;text-align:center;font-size:10px;font-style:italic;color:var(--wood-text)}

/* photos */
.photos{left:0;top:905px;width:1200px;height:595px;background:var(--photos-bg)}
.section-title{font-family:"Oswald",sans-serif;font-weight:500;font-size:24px;color:var(--wood-text);text-transform:uppercase}
.photos-title{left:230px;top:956px}
.photo-card-frame{left:243px;top:1019px;width:156px;height:202px;background:var(--white);box-shadow:0 1px 4px rgba(0,0,0,0.2)}
.photo{width:155px;height:155px}
.photo--pups{background:
  radial-gradient(ellipse 40px 34px at 60px 45px,rgba(255,255,255,0.9),rgba(255,255,255,0)),
  radial-gradient(ellipse 36px 30px at 110px 120px,rgba(255,255,255,0.85),rgba(255,255,255,0)),
  radial-gradient(ellipse 60px 50px at 70px 40px,#9a5f2e,rgba(154,95,46,0)),
  radial-gradient(ellipse 50px 45px at 120px 110px,#a3652f,rgba(163,101,47,0)),
  radial-gradient(ellipse 50px 50px at 25px 120px,#3a2e28,rgba(58,46,40,0)),
  linear-gradient(160deg,#f2ede8,#c9a98a)}
.photo--fence{background:
  radial-gradient(ellipse 60px 70px at 80px 95px,#c58b48,rgba(197,139,72,0)),
  radial-gradient(ellipse 45px 30px at 50px 25px,#d8a48c,rgba(216,164,140,0)),
  linear-gradient(160deg,#5f6e5a,#8c8c78 50%,#5a4a38)}
.photo--glasses{background:
  radial-gradient(ellipse 30px 40px at 95px 110px,#d9606a,rgba(217,96,106,0)),
  radial-gradient(ellipse 75px 80px at 70px 70px,#d69a4a,rgba(214,154,74,0)),
  linear-gradient(160deg,#ffffff,#f0e6d6)}
.photo--corgi{background:
  radial-gradient(ellipse 35px 45px at 80px 110px,#fbf8f4,rgba(251,248,244,0)),
  radial-gradient(ellipse 70px 80px at 75px 70px,#b2602a,rgba(178,96,42,0)),
  linear-gradient(160deg,#ffffff,#f1e7de)}
.photo-caption{width:155px;text-align:center;font-family:"Roboto Condensed",sans-serif;font-weight:700;font-size:14px;color:#2a2a2a}
.photo-caption--active{color:var(--wood-text)}

/* news */
.news{left:0;top:1500px;width:1200px;height:286px;background:var(--news-bg)}
.news-title{left:230px;top:1552px}
.news-photo{width:96px;height:97px;background:
  radial-gradient(ellipse 30px 38px at 48px 42px,#c48c6c,rgba(196,140,108,0)),
  radial-gradient(ellipse 60px 30px at 48px 100px,#1f2c4a,rgba(31,44,74,0)),
  linear-gradient(180deg,#8e9aa6 0%,#6e7a86 60%,#2b3a55 100%)}
.news-heading{font-family:"Roboto Condensed",sans-serif;font-weight:700;font-size:16px;color:var(--white);white-space:nowrap}
.news-date{font-size:8px;font-style:italic;font-weight:700;color:var(--white)}
.news-text{width:240px;font-size:8.3px;line-height:11.6px;color:#e8e8e8}
.btn-news{width:69px;height:20px;font-size:8.5px;color:var(--white);display:flex;align-items:center;justify-content:center;border-radius:2px}
.btn-news--dark{background:#4a4a4a;border:1px solid #777}
.btn-news--wood{background:var(--wood)}

/* footer */
.site-footer{left:0;top:1786px;width:1200px;height:330px;background:var(--footer-bg)}
.footer-heading{font-family:"Roboto Condensed",sans-serif;font-weight:700;font-size:14px;color:#2a2a2a;text-transform:uppercase;letter-spacing:0.3px}
.footer-list{list-style:none;font-size:11.5px;color:#333;line-height:19px}
.contact-row{font-size:11.5px;color:#333;line-height:21px;white-space:nowrap}
.contact-row span{display:inline-block;width:70px}
.brand--foot{left:760px;top:1842px;font-size:16px;gap:8px}
.brand--foot .brand-dot{width:14px;height:14px}
.footer-about{left:764px;top:1890px;width:200px;font-size:12px;line-height:17px;color:#333}
.footer-about p+p{margin-top:17px}

/* bottom bar */
.bottom-bar{left:0;top:2116px;width:1200px;height:55px;background:var(--bar-bg)}
.bottom-row{left:234px;top:2135px;display:flex;align-items:center;gap:12px;font-family:"Roboto Condensed",sans-serif;font-weight:700;font-size:12px;white-space:nowrap}
.bottom-site{color:var(--white)}
.bottom-sep{width:14px;height:14px;border-radius:50%;background:#3a3a3a}
.bottom-policy{color:var(--wood)}
.to-top{left:887px;top:2122px;width:51px;height:49px;background:var(--white);border-radius:3px 3px 0 0;display:flex;align-items:center;justify-content:center}
</style>
</head>
<body>

<header class="abs site-header"></header>
<div class="abs brand brand--head"><span class="brand-dot"></span>Larkfield Critter Depot</div>
<div class="abs tagline">Dedicated to a better diet for a healthier pet</div>
<div class="abs phone-icon">
  <svg width="18" height="18" viewBox="0 0 24 24"><path fill="#fff" d="M6.6 10.8c1.4 2.8 3.8 5.1 6.6 6.6l2.2-2.2c.3-.3.7-.4 1-.2 1.1.4 2.3.6 3.6.6.6 0 1 .4 1 1V20c0 .6-.4 1-1 1C10.6 21 3 13.4 3 4c0-.6.4-1 1-1h3.5c.6 0 1 .4 1 1 0 1.3.2 2.5.6 3.6.1.3 0 .7-.2 1z"/></svg>
</div>
<div class="abs phone-number">1300 555 018</div>

<nav class="abs main-nav"></nav>
<div class="abs nav-home"></div>
<a class="abs nav-item nav-item--active" style="left:271px">Home</a>
<a class="abs nav-item" style="left:352px">Events</a>
<a class="abs nav-item" style="left:431px">Blog</a>
<a class="abs nav-item" style="left:515px">About</a>
<a class="abs nav-item" style="left:606px">Dog Wash</a>
<a class="abs nav-item" style="left:697px">Resources</a>
<a class="abs nav-item nav-item--big" style="left:785px">Products</a>
<a class="abs nav-item" style="left:857px">Links</a>
<a class="abs nav-item" style="left:920px">Contact</a>

<section class="abs hero" role="img" aria-label="Night street with blurred bokeh lights above a weathered wooden floor"></section>
<div class="abs hero-dog" role="img" aria-label="Corgi lying on the wooden floor"></div>
<div class="abs hero-arrow hero-arrow--left">
  <svg width="18" height="34" viewBox="0 0 18 34"><path d="M15 2 L4 17 L15 32" fill="none" stroke="#c98f45" stroke-width="5"/></svg>
</div>
<div class="abs hero-arrow hero-arrow--right">
  <svg width="18" height="34" viewBox="0 0 18 34"><path d="M3 2 L14 17 L3 32" fill="none" stroke="#c98f45" stroke-width="5"/></svg>
</div>
<h1 class="abs hero-title">Welcome to <span>Larkfield Critter Depot</span></h1>
<p class="abs hero-text">Lorem ipsum dolor sit amet, consectetur adipisicing elit, sed do eiusmod tempor incididunt ut labore et dolore magna aliqua. Ut enim ad minim veniam, quis nostrud exercitation ullamco laboris nisi ut aliquip ex ea commodo consequat. Duis aute irure dolor in reprehenderit in voluptate velit</p>
<a class="abs btn-hero">Read More</a>
<span class="abs hero-dot hero-dot--on" style="left:269px"></span>
<span class="abs hero-dot" style="left:295px"></span>
<span class="abs hero-dot" style="left:323px"></span>

<section class="abs features"></section>
<article class="abs feature" style="left:221px">
  <div class="feature-icon"><svg width="30" height="28" viewBox="0 0 30 28"><path d="M15 2 L28 14 H24 V26 H18 V18 H12 V26 H6 V14 H2 Z" fill="#fff"/></svg></div>
  <h2 class="feature-title">Lorem ipsumdolor</h2>
  <p class="feature-text">Lorem ipsum dolor sit amet, consectetur adipisicing elit, sed do eiusmod tempor incididunt ut labore et dolore magna aliqua. Ut enim ad minim veniam, quis nostrud exercitation ullamco laboris nisi ut aliquip ex ea commodo consequat. Duis</p>
  <a class="feature-more">Continue reading...</a>
</article>
<article class="abs feature" style="left:475px">
  <div class="feature-icon"><svg width="28" height="30" viewBox="0 0 28 30"><circle cx="14" cy="11" r="9" fill="#fff"/><circle cx="14" cy="11" r="5" fill="none" stroke="#d2b883" stroke-width="2"/><path d="M8 18 L6 29 L14 25 L22 29 L20 18 Z" fill="#fff"/></svg></div>
  <h2 class="feature-title">Lorem ipsumdolor</h2>
  <p class="feature-text">Lorem ipsum dolor sit amet, consectetur adipisicing elit, sed do eiusmod tempor incididunt ut labore et dolore magna aliqua. Ut enim ad minim veniam, quis nostrud exercitation ullamco laboris nisi ut aliquip ex ea commodo consequat. Duis</p>
  <a class="feature-more">Continue reading...</a>
</article>
<article class="abs feature" style="left:728px">
  <div class="feature-icon"><svg width="30" height="26" viewBox="0 0 30 26"><rect x="10" y="1" width="10" height="6" rx="1" fill="none" stroke="#fff" stroke-width="2"/><rect x="2" y="6" width="26" height="19" rx="2" fill="#fff"/><path d="M13 10 H17 V14 H21 V18 H17 V22 H13 V18 H9 V14 H13 Z" fill="#d2b883"/></svg></div>
  <h2 class="feature-title">Lorem ipsumdolor</h2>
  <p class="feature-text">Lorem ipsum dolor sit amet, consectetur adipisicing elit, sed do eiusmod tempor incididunt ut labore et dolore magna aliqua. Ut enim ad minim veniam, quis nostrud exercitation ullamco laboris nisi ut aliquip ex ea commodo consequat. Duis</p>
  <a class="feature-more">Continue reading...</a>
</article>

<section class="abs photos"></section>
<h2 class="abs section-title photos-title">Latest Photos</h2>
<div class="abs photo-card-frame"></div>

<div class="abs photo photo--pups" style="left:244px;top:1020px" role="img" aria-label="Group of puppies"></div>
<div class="abs photo photo--fence" style="left:428px;top:1020px" role="img" aria-label="Golden dog by a fence"></div>
<div class="abs photo photo--glasses" style="left:614px;top:1020px" role="img" aria-label="Golden retriever wearing glasses"></div>
<div class="abs photo photo--corgi" style="left:798px;top:1020px" role="img" aria-label="Corgi portrait"></div>
<div class="abs photo-caption photo-caption--active" style="left:244px;top:1186px">Take a closer look.</div>
<div class="abs photo-caption" style="left:428px;top:1186px">Take a closer look.</div>
<div class="abs photo-caption" style="left:614px;top:1186px">Take a closer look.</div>
<div class="abs photo-caption" style="left:798px;top:1186px">Take a closer look.</div>

<div class="abs photo photo--pups" style="left:244px;top:1247px" role="img" aria-label="Group of puppies"></div>
<div class="abs photo photo--fence" style="left:428px;top:1247px" role="img" aria-label="Golden dog by a fence"></div>
<div class="abs photo photo--glasses" style="left:614px;top:1247px" role="img" aria-label="Golden retriever wearing glasses"></div>
<div class="abs photo photo--corgi" style="left:798px;top:1247px" role="img" aria-label="Corgi portrait"></div>
<div class="abs photo-caption" style="left:244px;top:1413px">Take a closer look.</div>
<div class="abs photo-caption" style="left:428px;top:1413px">Take a closer look.</div>
<div class="abs photo-caption" style="left:614px;top:1413px">Take a closer look.</div>
<div class="abs photo-caption" style="left:798px;top:1413px">Take a closer look.</div>

<section class="abs news"></section>
<h2 class="abs section-title news-title">News &amp; Events</h2>
<div class="abs news-photo" style="left:237px;top:1604px" role="img" aria-label="Portrait of a man in a suit"></div>
<h3 class="abs news-heading" style="left:352px;top:1606px">Take a closer look.</h3>
<div class="abs news-date" style="left:352px;top:1627px">Aug 17, 2012 • 4</div>
<p class="abs news-text" style="left:352px;top:1646px">Proin gravida nibh vel velit auctor aliquet. Aenean sollicitudin, lorem quis bibendum auctor, nisi elit consequat ipsum, nec sagittis sem nibh id elit. Duis sed odio sit amet nibh vulputate cursus a sit amet.consequat</p>
<a class="abs btn-news btn-news--dark" style="left:352px;top:1706px">Read More</a>

<div class="abs news-photo" style="left:617px;top:1604px" role="img" aria-label="Portrait of a man in a suit"></div>
<h3 class="abs news-heading" style="left:731px;top:1606px">Take a closer look.</h3>
<div class="abs news-date" style="left:731px;top:1627px">Aug 17, 2012 • 4</div>
<p class="abs news-text" style="left:731px;top:1646px">Proin gravida nibh vel velit auctor aliquet. Aenean sollicitudin, lorem quis bibendum auctor, nisi elit consequat ipsum, nec sagittis sem nibh id elit. Duis sed odio sit amet nibh vulputate cursus a sit amet.consequat</p>
<a class="abs btn-news btn-news--wood" style="left:729px;top:1706px">Read More</a>

<footer class="abs site-footer"></footer>
<h4 class="abs footer-heading" style="left:234px;top:1848px">Company</h4>
<ul class="abs footer-list" style="left:234px;top:1876px">
  <li>Home</li><li>Events</li><li>Blog</li><li>About</li><li>Dog Wash</li><li>Resources</li><li>Products</li><li>Link</li><li>Contact</li>
</ul>
<h4 class="abs footer-heading" style="left:394px;top:1845px">Follow us</h4>
<ul class="abs footer-list" style="left:394px;top:1876px;line-height:21.5px">
  <li>Chatterly</li><li>Pipwire</li><li>Frondbook</li><li>Workloop</li><li>RSS</li>
</ul>
<h4 class="abs footer-heading" style="left:544px;top:1845px">Contact us</h4>
<div class="abs" style="left:544px;top:1875px">
  <div class="contact-row"><span>Telephone</span>+1400 555 019</div>
  <div class="contact-row"><span>FAX</span>+1504 555 0142</div>
  <div class="contact-row"><span>E-mail</span>larkfieldcritterdepot.com</div>
</div>
<div class="abs brand brand--foot"><span class="brand-dot"></span>Larkfield Critter Depot</div>
<div class="abs footer-about">
  <p>Your about us information would fit here nicely.</p>
  <p>You could also just have an overview and use the link below to link to you full about us page.</p>
</div>

<div class="abs bottom-bar"></div>
<div class="abs bottom-row">
  <span class="bottom-site">LARKFIELDCRITTERDEPOT.COM</span>
  <span class="bottom-sep"></span>
  <span class="bottom-policy">2015 PRIVACY POLICY</span>
</div>
<a class="abs to-top" aria-label="Back to top">
  <svg width="24" height="24" viewBox="0 0 24 24"><path d="M12 3 L22 13 H15 V22 H9 V13 H2 Z" fill="#222"/></svg>
</a>

</body>
</html>
```